Stories from Elm trifold brochure design

We are a start up company that will help seniors write their memoirs...beginning with a few ancestors and their heritage and continuing through their own history...how they would like to be remembered in the next generation. I envision a senior citizen at an older writing desk, writing her memoirs, with a book (maybe standing on top, leaning slightly) that has the words Stories from Elm.com on the back binding. OR maybe a senior couple walking into the sunset with the same book somewhere in the frame. Communicating the relevance of every life being significant to those that come after them...when a genealogy doesn't say enough about the details of one's life. Please note that I am open to the professionals own ideas...I am not locked into my concepts. I would like one or two phrases..."When A Genealogy Doesn't Say Enough" and/or "Every life legacy is a gift for the next generation to treasure" to be in the design.
A few documents are loaded that contain notes for our web designers. Maybe they will help you with our thoughts.

Reason: We have added some additional photos that might be useful.

Target Market(s)

Seniors and the baby boomer generation

Industry/Entity Type

Graphic Design

Requirements
Must have
• Stories from Elm
• Doris Whitcombe, M.A.
• 1-609-382-5171 (local)
• 1-866-4TALEKP (toll free)
• info@storiesfromelm.com
• storiesfromelm.com
Should not have
• Scripts that would be challenging for seniors to read.

```html
<!DOCTYPE html>
<html lang="en">
<head>
<meta charset="utf-8">
<title>Stories from Elm – Trifold Brochure</title>
<link rel="stylesheet" href="https://fonts.googleapis.com/css2?family=Asap:wght@400;600;700&family=Kaushan+Script&display=swap">
<style>
  :root {
    --page-bg: #e4e4e4;
    --sky-top: #a9c4c8;
    --sky-mid: #d9d2bf;
    --sand: #ead6b4;
    --ink: #2f2a28;
    --ink-soft: #4a423d;
    --gold: #b8952f;
    --gold-deep: #9c7d24;
    --gold-light: #d4af47;
    --table-head: #b39a3e;
    --table-label: #d9cfbe;
    --table-cell: #f7f4ee;
    --white: #ffffff;
    --cover-brown: #4b2c22;
    --cover-text: #efe3cf;
  }
  * { box-sizing: border-box; margin: 0; padding: 0; }
  html, body { width: 1200px; height: 795px; overflow: hidden; }
  body {
    background: var(--page-bg);
    font-family: "Asap", "Helvetica Neue", Arial, sans-serif;
    color: var(--ink);
    position: relative;
  }

  /* Inside spread */
  .inside-spread {
    position: absolute; left: 60px; top: 98px;
    width: 780px; height: 600px;
    display: flex;
    background: linear-gradient(180deg, var(--sky-top) 0%, var(--sky-mid) 45%, var(--sand) 100%);
    box-shadow: 0 6px 18px rgba(0,0,0,.18);
  }
  .panel { position: relative; width: 260px; height: 100%; }
  .panel + .panel { border-left: 1px solid rgba(0,0,0,.06); }

  /* Left panel */
  .intro-panel { padding: 30px 22px 0; }
  .dot-rule { text-align: center; color: var(--white); letter-spacing: 2px; font-size: 9px; }
  .headline-quote {
    font-family: "Kaushan Script", cursive;
    color: var(--white); text-align: center; font-weight: 400;
    font-size: 25px; line-height: 1.25; margin: 8px 0 6px;
  }
  .intro-question { font-weight: 700; font-size: 11.5px; line-height: 1.35; margin-top: 22px; }
  .intro-text { font-size: 10px; line-height: 1.4; color: var(--ink-soft); margin-top: 8px; }
  .intro-text strong { color: var(--ink); }
  .couple-photo {
    position: absolute; left: 0; bottom: 0; width: 260px; height: 280px;
    background: linear-gradient(180deg, #c9b9a4 0%, #a99682 30%, #6f6a66 55%, #5a4a3d 100%);
  }

  /* Offer area spanning centre and right panels */
  .offer-area {
    position: absolute; left: 260px; top: 0; width: 520px; height: 100%;
    padding: 30px 26px 0; text-align: center;
  }
  .offer-lead { font-size: 12px; color: var(--ink-soft); line-height: 1.3; }
  .offer-lead em { font-style: italic; font-weight: 600; color: var(--gold); }
  .lives-row { display: flex; align-items: center; justify-content: space-between; margin-top: 20px; }
  .script-heading { font-family: "Kaushan Script", cursive; font-weight: 400; color: var(--gold); font-size: 21px; line-height: 1.2; width: 150px; }
  .portrait-photo {
    width: 88px; height: 88px; border-radius: 10px;
    background: linear-gradient(160deg, #6d5a4c 0%, #3c2e27 60%, #241a16 100%);
  }
  .options-row { display: flex; justify-content: space-between; align-items: center; margin-top: 26px; }
  .option { width: 140px; font-size: 10px; line-height: 1.35; color: var(--ink-soft); }
  .option-or { font-size: 9px; color: var(--gold); font-weight: 600; }
  .packages-intro { font-size: 10.5px; font-weight: 600; margin-top: 30px; line-height: 1.35; }

  .package-table {
    width: 430px; margin: 14px auto 0; border-collapse: collapse;
    font-size: 9.5px; line-height: 1.4;
  }
  .package-table th {
    background: var(--table-head); color: var(--white);
    font-weight: 600; font-size: 12.5px; height: 34px;
    border-right: 1px solid rgba(255,255,255,.5);
  }
  .package-table td { background: var(--table-cell); padding: 8px 8px; border: 1px solid #e5ddcf; }
  .package-table td.row-label { background: var(--table-label); font-weight: 600; text-align: left; padding-left: 22px; width: 96px; }

  /* Front cover panel */
  .front-cover {
    position: absolute; left: 880px; top: 98px;
    width: 260px; height: 600px;
    background: var(--cover-brown);
    box-shadow: 0 6px 18px rgba(0,0,0,.18);
    overflow: hidden;
  }
  .cover-photo {
    position: absolute; left: 0; top: 0; width: 100%; height: 100%;
    background: linear-gradient(180deg, #6b4a39 0%, #5a3a2c 30%, #7b5a44 55%, #3d241b 100%);
  }
  .cover-frame { position: absolute; inset: 12px; border: 1px solid rgba(214,176,90,.45); }
  .brand-card {
    position: absolute; left: 30px; top: 30px; width: 200px; height: 140px;
    background: var(--white); border-radius: 6px;
    display: flex; align-items: center; justify-content: center;
  }
  .brand-name { font-weight: 600; font-size: 22px; color: var(--gold-deep); }
  .contact-block {
    position: absolute; left: 24px; right: 24px; bottom: 72px;
    text-align: center; color: var(--cover-text);
    font-size: 11px; line-height: 1.55;
  }
  .contact-name { font-weight: 600; font-size: 13px; color: var(--gold-light); margin-bottom: 4px; }
  .cover-tagline {
    position: absolute; left: 0; right: 0; bottom: 30px;
    text-align: center; font-style: italic; font-size: 15px; color: var(--gold-light);
  }
</style>
</head>
<body>
  <section class="inside-spread">
    <div class="panel intro-panel">
      <p class="dot-rule">••••••••••••••••••••</p>
      <h1 class="headline-quote">“When a genealogy doesn’t say enough!”</h1>
      <p class="dot-rule">••••••••••••••••••••</p>
      <p class="intro-question">If you were alive in 100 years, what would you share with your descendants?</p>
      <p class="intro-text">Now you have a vehicle to help you immortalize your thoughts for the future... <strong>specifically for those who will want to know!</strong></p>
      <div class="couple-photo" role="img" aria-label="Photo of a senior couple walking along a beach at sunset"></div>
    </div>
    <div class="panel"></div>
    <div class="panel"></div>

    <div class="offer-area">
      <p class="offer-lead">We are not all presidents of countries or CEO’s of fortune 500 companies!<br>But <em>“every life legacy is a gift to be treasured by the next generation.”</em></p>
      <div class="lives-row">
        <h2 class="script-heading">Ordinary<br>Lives</h2>
        <div class="portrait-photo" role="img" aria-label="Photo of an elderly man holding his finished memoir book"></div>
        <h2 class="script-heading">Extraordinary<br>Legacies</h2>
      </div>
      <div class="options-row">
        <p class="option">You can provide the majority of input in an organized fashion (as specified by Stories from Elm).</p>
        <span class="option-or">OR</span>
        <p class="option">We help organize photos and interview one-on-one for history</p>
        <span class="option-or">OR</span>
        <p class="option">Bring friends together for a 12 week program so we can help you on your way</p>
      </div>
      <p class="packages-intro">Choose one of our three packages and decide how much you want us to participate for<br>the best price to meet your needs.</p>
      <table class="package-table">
        <thead>
          <tr><th></th><th>PACKAGE I</th><th>PACKAGE II</th><th>PACKAGE III</th></tr>
        </thead>
        <tbody>
          <tr>
            <td class="row-label">Description</td>
            <td>Standard Portrait book with up to 120 pages or 18,000 words</td>
            <td>Standard Trade book upto 250 pages or 100,000 words</td>
            <td>Standard Portrait book with 120 or 200 pages or 18,000 to 30,000 words</td>
          </tr>
          <tr><td class="row-label">Size</td><td>6 x 9 in</td><td>6 x 9 in</td><td>6 x 9 in</td></tr>
          <tr><td class="row-label">Contents</td><td>Text &amp; photos</td><td>Text &amp; photos</td><td>Text &amp; photos</td></tr>
        </tbody>
      </table>
    </div>
  </section>

  <section class="front-cover">
    <div class="cover-photo" role="img" aria-label="Photo of a senior woman writing her memoirs at an old wooden writing desk by lamplight"></div>
    <div class="cover-frame"></div>
    <div class="brand-card"><span class="brand-name">Stories from Elm</span></div>
    <address class="contact-block">
      <p class="contact-name">Doris Whitcombe, M.A.</p>
      <p>1-609-382-5171 (local)</p>
      <p>1-866-4TALEKP (toll free)</p>
      <p>info@storiesfromelm.com</p>
      <p>storiesfromelm.com</p>
    </address>
    <p class="cover-tagline">Encouragement for the Believer</p>
  </section>
</body>
</html>
```